Infographic Template that Showcases individual wine producers of the World

Needs to be an infographic template A4 size. Allowing Winemaker introduction, Location (with Map) Climate, Soils, Winemaking methods, and Varietals Grown. This template will be applied to wines we focus as a part of our restaurant wine experience. Colour Focus should be red, white and black. An example of some italian wine makers is shown in the images. Though I would prefer that it is not black background but essentially has these sections and is clean with the ability to add specific text, images and maps.

Target Market(s)

Our Guests at the restaurant as a take away during a wine experience event

Industry/Entity Type

Hospitality

Font styles to use
Sans Serif

Colors
EB3D1F
EC4F4E
F09395
F8D3D4
FCEDEE

Requirements
Must have
• Must be a templaate so we can add winegrowers details when we offer the wine
Nice to have
• Nice for the infographic design to be unique, carry our logo, attached and be clean lines and print well on A4 or greater

```html
<!DOCTYPE html>
<html lang="it">
<head>
<meta charset="utf-8">
<title>Scheda Vino – Bramaterra</title>
<link href="https://fonts.googleapis.com/css2?family=Oswald:wght@400;500&family=Poppins:wght@400;500;600;700&display=swap" rel="stylesheet">
<style>
:root{
  --red:#e0141b;
  --red-soft:#ec4f4e;
  --ink:#1f1f1f;
  --band:#2b2b2b;
  --paper:#ffffff;
  --backdrop:#e9e9e9;
  --grey:#8a8a8a;
}
*{box-sizing:border-box;margin:0;padding:0}
html,body{width:843px;height:1200px;overflow:hidden;background:var(--backdrop)}
body{position:relative;font-family:"Poppins",Arial,sans-serif;color:var(--ink)}
.page{position:absolute;left:213px;width:595px;height:842px;background:var(--paper);
  transform:scale(0.7);transform-origin:0 0;overflow:hidden}
.page--front{top:8px}
.page--back{top:603px}
.abs{position:absolute}
.illus{position:absolute;border-radius:6px}
.brand{position:absolute;left:30px;top:52px;z-index:2;display:flex;align-items:center;gap:12px;
  font-family:"Poppins",sans-serif;font-weight:600;font-size:16px;line-height:20px;letter-spacing:2px;color:var(--ink)}
.brand__dot{width:44px;height:44px;border-radius:50%;background:var(--red);flex:none}
.brand__name{display:flex;flex-direction:column}
.title-band{position:absolute;background:var(--red);color:#fff;font-family:"Oswald",sans-serif;
  font-weight:500;line-height:1;padding-left:46px;display:flex;align-items:center}
.meta{position:absolute;font-size:16px;line-height:21.5px}
.meta b{font-weight:500}
.dark-band{position:absolute;background:var(--band)}
.pct{position:absolute;width:66px;height:66px;border-radius:50%;background:var(--red);border:2px solid #fff;
  color:#fff;font-weight:700;font-size:27px;display:flex;align-items:center;justify-content:center}
.pct sup{font-size:12px;margin-top:-12px}
.pct-label{position:absolute;width:110px;text-align:center;color:#fff;font-size:15px}
.heading{position:absolute;font-family:"Oswald",sans-serif;font-size:21px;font-weight:500;color:var(--ink)}
.heading em{font-style:normal;color:var(--red)}
.chip{position:absolute;left:30px;height:28px;background:var(--red);color:#fff;font-size:16px;
  display:flex;align-items:center;padding-left:17px;font-weight:500}
.chip strong{font-size:21px;font-weight:700;margin:0 2px}
.dash{position:absolute;border-top:1.5px dashed #999}
.bullets{position:absolute;list-style:none;font-size:16px;line-height:25px}
.bullets li{display:flex;align-items:center;gap:7px}
.bullets li::before{content:"";width:11px;height:11px;border-radius:50%;background:var(--red)}
.footer{position:absolute;left:0;bottom:0;width:595px;height:52px;background:var(--band);color:#fff;
  font-size:15px;letter-spacing:4px;display:flex;align-items:center;justify-content:center;padding-bottom:20px}
.body-text{position:absolute;font-size:17px;line-height:20px}
.scale-label{position:absolute;font-size:15px}
.note-label{position:absolute;color:var(--red);font-size:12px;font-weight:500}
.note-text{position:absolute;font-size:8px;line-height:10px}
</style>
</head>
<body>

<section class="page page--front">
  <div class="brand"><span class="brand__dot"></span><span class="brand__name"><span>ASHFORD</span><span>KITCHEN &amp; BAR</span></span></div>
  <div class="illus" role="img" aria-label="Vine leaves and dark grape clusters" style="left:320px;top:0;width:275px;height:140px;border-radius:0 0 0 80px;background:linear-gradient(200deg,#a9cf4a,#e6efc8 55%,#fff)"></div>

  <div class="title-band" style="left:70px;top:170px;width:298px;height:38px;font-size:36px">BRAMATERRA</div>
  <div class="illus" role="img" aria-label="Red wine bottle with a filled glass" style="left:40px;top:152px;width:62px;height:140px;background:linear-gradient(180deg,#7a1515,#3d0d0d)"></div>
  <div class="meta" style="left:117px;top:218px">
    <div><b>Produttore:</b>&nbsp;&nbsp; Valbruna</div>
    <div><b>Tipologia:</b>&nbsp;&nbsp; Bramaterra DOC</div>
    <div><b>Produttore:</b>&nbsp;&nbsp; Valbruna</div>
  </div>
  <div class="illus" role="img" aria-label="Map of north-west Italy with the Bramaterra area highlighted in red" style="left:392px;top:148px;width:178px;height:158px;background:linear-gradient(120deg,#e0141b 0 28%,#555 28%)"></div>
  <div class="abs" style="left:398px;top:272px;font-size:9px">Bramaterra</div>

  <div class="dark-band" style="left:28px;top:312px;width:536px;height:110px"></div>
  <div class="illus" role="img" aria-label="Bottle of brandy beside white grapes" style="left:38px;top:320px;width:62px;height:94px;background:linear-gradient(180deg,#d88a2a,#7a4512)"></div>
  <div class="abs" style="left:108px;top:312px;width:2px;height:110px;background:#fff"></div>
  <div class="abs" style="left:108px;top:312px;width:28px;height:110px;display:flex;align-items:center;justify-content:center">
    <span style="transform:rotate(-90deg);color:#fff;font-family:Oswald,sans-serif;font-size:22px;font-weight:500;white-space:nowrap">UVAGGIO</span>
  </div>
  <div class="pct" style="left:165px;top:324px">70<sup>%</sup></div>
  <div class="pct" style="left:261px;top:324px">20<sup>%</sup></div>
  <div class="pct" style="left:356px;top:324px">7<sup>%</sup></div>
  <div class="pct" style="left:456px;top:324px">3<sup>%</sup></div>
  <div class="pct-label" style="left:144px;top:396px">Nebbiolo</div>
  <div class="pct-label" style="left:240px;top:396px">Croatina</div>
  <div class="pct-label" style="left:334px;top:396px">Vespolina</div>
  <div class="pct-label" style="left:434px;top:396px">Uva Rara</div>

  <div class="heading" style="left:28px;top:448px"><em>TERROIR:</em> COLLINARE</div>
  <div class="chip" style="top:487px;width:365px">Terreni minerali con residui morenici</div>
  <div class="chip" style="top:525px;width:298px">Altitudine&nbsp;<strong>370-440</strong>&nbsp;m.s.l.m.</div>
  <div class="chip" style="top:563px;width:283px">Esposizione Sud - Sud Ovest</div>
  <div class="chip" style="top:602px;width:210px">Pendenza&nbsp;<strong>20-35%</strong></div>
  <div class="illus" role="img" aria-label="Wine bottle, glass of red wine, vine leaves and black grapes" style="left:372px;top:440px;width:198px;height:200px;background:linear-gradient(160deg,#6da33a,#4a1a14 55%,#2a0f2e)"></div>

  <div class="dash" style="left:30px;top:661px;width:533px"></div>
  <div class="illus" role="img" aria-label="Globe with thermometer" style="left:28px;top:675px;width:78px;height:75px;border-radius:50%;background:radial-gradient(circle,#8cc4e6,#4d8a3a)"></div>
  <div class="heading" style="left:124px;top:672px"><em>CLIMA:</em> CONTINENTALE ALPINO</div>
  <ul class="bullets" style="left:126px;top:705px">
    <li>Estati calde e inverni freddi</li>
    <li>importamte escursione termica</li>
    <li>brezza pomeridiana costante</li>
  </ul>
  <div class="illus" role="img" aria-label="Bunch of green grapes" style="left:448px;top:700px;width:88px;height:68px;border-radius:40%;background:radial-gradient(circle,#c5e07a,#7aa83a)"></div>

  <div class="footer">WWW.ASHFORDKITCHEN.COM.AU</div>
</section>

<section class="page page--back">
  <div class="brand"><span class="brand__dot"></span><span class="brand__name"><span>ASHFORD</span><span>KITCHEN &amp; BAR</span></span></div>
  <div class="illus" role="img" aria-label="Vine leaves and dark grape clusters" style="left:320px;top:0;width:275px;height:175px;border-radius:0 0 0 80px;background:linear-gradient(200deg,#a9cf4a,#e6efc8 55%,#fff)"></div>

  <div class="title-band" style="left:112px;top:145px;width:305px;height:38px;font-size:36px;padding-left:36px">VINITICAZIONE</div>
  <div class="illus" role="img" aria-label="Stacked wooden wine barrels with grapes" style="left:22px;top:140px;width:124px;height:135px;border-radius:50%;background:radial-gradient(circle,#e7a35e,#a8642a)"></div>
  <div class="body-text" style="left:155px;top:186px">Vendemmia manuale, a<br>fermentazione spontanea con in<br>vasche di cemento vetrificato<br>interrateper circa 20 giorni. (anno 1920)</div>
  <div class="body-text" style="left:152px;top:273px;width:400px;text-align:center"><b style="font-weight:500">Atfinamento:</b> in botti di rovere grandi per circa<br>30 mesi</div>

  <div class="dark-band" style="left:30px;top:338px;width:277px;height:64px"></div>
  <div class="abs" style="left:45px;top:356px;color:#fff;font-family:Oswald,sans-serif;font-size:21px;font-weight:500">LIEVITI SELVAGGI</div>
  <div class="illus" role="img" aria-label="Pile of wild yeast granules" style="left:238px;top:348px;width:60px;height:44px;border-radius:40%;background:radial-gradient(circle,#c9a27a,#6e4e37)"></div>
  <div class="illus" role="img" aria-label="Row of empty, red and white wine glasses" style="left:334px;top:318px;width:226px;height:88px;background:linear-gradient(90deg,#eee,#e8e8e8 40%,#8a1420 60%,#8a1420 78%,#f2e6a8)"></div>

  <div class="heading" style="left:27px;top:420px;color:var(--red)">RESIDUO ZUCCHERINO:</div>
  <div class="scale-label" style="left:30px;top:456px">Secco 0-10 g/l</div>
  <div class="scale-label" style="left:219px;top:456px">Amabile 30-50 g/l</div>
  <svg class="abs" style="left:30px;top:483px" width="535" height="10" viewBox="0 0 535 10">
    <rect x="0" y="0" width="180" height="8" fill="#2b2b2b"/>
    <rect x="0" y="0" width="73" height="8" fill="#e0141b"/>
    <rect x="184" y="0" width="162" height="8" fill="#2b2b2b"/>
    <rect x="350" y="0" width="185" height="8" fill="#2b2b2b"/>
  </svg>
  <div class="scale-label" style="left:145px;top:499px">Abboccato 10-30 g/l</div>
  <div class="scale-label" style="left:406px;top:499px">Dolce 50-180 g/l</div>

  <div class="dark-band" style="left:0;top:538px;width:595px;height:79px"></div>
  <div class="abs" style="left:112px;top:577px;width:375px;height:2px;background:#fff"></div>
  <div class="pct" style="left:48px;top:545px">6<sup>%</sup></div>
  <div class="pct" style="left:484px;top:545px">22<sup>%</sup></div>
  <div class="abs" style="left:158px;top:562px;width:279px;height:30px;background:var(--red);color:#fff;font-family:Oswald,sans-serif;font-size:20px;font-weight:500;display:flex;align-items:center;justify-content:center;letter-spacing:.5px">GRADO ALCOLICO: 14.5%</div>

  <div class="heading" style="left:30px;top:634px;color:var(--red)">LONGEVITA CONSIGLIATA</div>
  <svg class="abs" style="left:32px;top:667px" width="26" height="26" viewBox="0 0 26 26">
    <circle cx="13" cy="13" r="11.5" fill="#e0141b" stroke="#1f1f1f" stroke-width="2"/>
    <path d="M13 6v7l-4 3" stroke="#fff" stroke-width="2" fill="none" stroke-linecap="round"/>
  </svg>
  <div class="heading" style="left:66px;top:666px;font-size:19px;font-weight:400">10-16 ANNI</div>
  <div class="dash" style="left:30px;top:708px;width:333px"></div>
  <div class="note-label" style="left:30px;top:718px">NOTE</div>
  <div class="note-text" style="left:30px;top:735px;width:340px">E dal 1977 che Ernesto e il figlio Luca Valbruna hanno ripreso in mano l'azienda coltivando i pochi ettari di proprieta nel pieno rispetto per la natura, infatti in vigna non vengono utilizzati diserbanti, ma solo piccole quantita di rame e zolfo.</div>
  <div class="illus" role="img" aria-label="Group of wine and spirit bottles with filled glasses" style="left:380px;top:636px;width:186px;height:150px;background:linear-gradient(90deg,#2f6b2a,#f3e6a2 40%,#c23a4a 65%,#1f1f1f 80%,#f2a63a)"></div>

  <div class="footer">WWW.ASHFORDKITCHEN.COM.AU</div>
</section>

</body>
</html>
```